Business Card Design Competition

We need a business card design for our Internet Marketing company. We require both front and back designs and the final card must be 89x53mm in size, plus crop marks to 91x55mm. Colours as per logo, plus perhaps black and/or grey (#828282).
Final text must be editable (if you can supply an editable Fireworks PNG, even better)...
FRONT TEXT:
Full Name
Position
Address Line
Suburb, State, Postcode
Phone: 0000 000 000
Mobile: 0000 000 000
Email: xxx@brimleafpromo.com.au
Web: www.brimleafpromo.com.au
Rear of card should be a fresh design plus our slogan text: "Getting You Noticed" in large font, then in small text "Brimleaf Holdings Pty Ltd (ABN: 42 563 701 384)".
Target Market(s)
Small/Medium Businesses
Industry/Entity Type
Business
Look and feel
Each slider illustrates characteristics of the customer's brand and the style your logo design should communicate.

```html
<!DOCTYPE html>
<html lang="en">
<head>
<meta charset="utf-8">
<title>Brimleaf Promo – Business Card Front</title>
<link rel="stylesheet" href="https://fonts.googleapis.com/css2?family=Source+Sans+3:wght@400;600;700&display=swap">
<style>
  :root {
    --card-black: #050505;
    --card-charcoal: #2b2b2b;
    --leaf-green: #8dc63f;
    --leaf-lime: #c8e021;
    --leaf-deep: #2f5a10;
    --accent-orange: #f7941d;
    --text-light: #d8d8d8;
    --text-grey: #bdbdbd;
  }
  * { margin: 0; padding: 0; box-sizing: border-box; }
  html, body {
    width: 720px;
    height: 1200px;
    overflow: hidden;
    background: var(--card-black);
  }
  .card {
    position: relative;
    width: 720px;
    height: 1200px;
    overflow: hidden;
    font-family: "Source Sans 3", "Myriad Pro", sans-serif;
    background:
      repeating-linear-gradient(90deg, rgba(255,255,255,0.018) 0 2px, transparent 2px 6px),
      radial-gradient(ellipse 70% 55% at 50% 48%, var(--card-charcoal) 0%, #121212 60%, var(--card-black) 100%);
  }
  .wave {
    position: absolute;
    left: 0;
    width: 720px;
    display: block;
  }
  .wave--top { top: 0; height: 330px; }
  .wave--bottom { bottom: 0; height: 250px; }

  .brand {
    position: absolute;
    left: 78px;
    top: 344px;
    display: flex;
    align-items: center;
    gap: 26px;
  }
  .brand__dot {
    width: 186px;
    height: 186px;
    border-radius: 50%;
    background: var(--accent-orange);
  }
  .brand__name {
    color: var(--leaf-green);
    font-weight: 600;
    font-size: 66px;
    line-height: 0.95;
    letter-spacing: 1px;
  }

  .person {
    position: absolute;
    top: 580px;
    left: 0;
    width: 720px;
    text-align: center;
  }
  .person__name {
    font-weight: 700;
    font-size: 70px;
    line-height: 1;
    letter-spacing: -1px;
  }
  .person__first { color: var(--leaf-green); }
  .person__last { color: var(--accent-orange); }
  .person__title {
    margin-top: 2px;
    color: var(--text-light);
    font-size: 29px;
    font-weight: 400;
  }

  .contact {
    position: absolute;
    left: 0;
    width: 720px;
    text-align: center;
    color: var(--text-grey);
    font-size: 27px;
    line-height: 36px;
  }
  .contact--address { top: 726px; }
  .contact--phones { top: 810px; }
  .contact--online { top: 897px; }
  .label--green { color: var(--leaf-green); }
  .label--orange { color: var(--accent-orange); }
</style>
</head>
<body>
<main class="card">
  <svg class="wave wave--top" viewBox="0 0 720 330" role="img" aria-label="Abstract flowing green and lime light waves across the top edge">
    <defs>
      <linearGradient id="topWaveFill" x1="0" y1="0" x2="1" y2="1">
        <stop offset="0" stop-color="#4f8a12"/>
        <stop offset="0.45" stop-color="#b6d62a"/>
        <stop offset="0.8" stop-color="#5c9a16"/>
        <stop offset="1" stop-color="#1d3608"/>
      </linearGradient>
    </defs>
    <path d="M0 0 H720 V150 C640 230 560 320 430 318 C310 316 250 230 150 215 C90 206 40 225 0 250 Z" fill="url(#topWaveFill)"/>
  </svg>

  <div class="brand">
    <div class="brand__dot"></div>
    <div class="brand__name">Brimleaf<br>Promo</div>
  </div>

  <section class="person">
    <h1 class="person__name"><span class="person__first">JOHN</span> <span class="person__last">SMITH</span></h1>
    <p class="person__title">Special Job Title</p>
  </section>

  <p class="contact contact--address">Address Line<br>Suburb, State, Postcode</p>
  <p class="contact contact--phones"><span class="label--green">Phone:</span> 0000 000 000<br><span class="label--green">Mobile:</span> 0000 000 000</p>
  <p class="contact contact--online"><span class="label--orange">Email:</span> xxx@brimleafpromo.com.au<br><span class="label--orange">Web:</span> www.brimleafpromo.com.au</p>

  <svg class="wave wave--bottom" viewBox="0 0 720 250" role="img" aria-label="Abstract flowing green and yellow light waves across the bottom edge">
    <defs>
      <linearGradient id="bottomWaveFill" x1="0" y1="0" x2="1" y2="1">
        <stop offset="0" stop-color="#2f5a10"/>
        <stop offset="0.4" stop-color="#8dbb1c"/>
        <stop offset="0.7" stop-color="#d8e02a"/>
        <stop offset="1" stop-color="#4f8a12"/>
      </linearGradient>
    </defs>
    <path d="M0 20 C120 60 190 150 330 140 C460 130 560 40 720 60 V250 H0 Z" fill="url(#bottomWaveFill)"/>
  </svg>
</main>
</body>
</html>
```